New Jar Label for Manuka Honey Company!

Hine Roa Honey, a Manuka Honey company from New Zealand is looking for a fresh & engaging label for our manuka honey jars.

Attached are some examples of label designs that we like, feel free to use the language/copy on these labels for inspiration/content/copy, but feel free to add your own creative spin if you have a great design idea!

LABEL DIMENSIONS: 1654mmx532mm

Label Must Include:
- MGO rating
- Made (or) Product of New Zealand
- Manuka Honey (can add extra text similar to attached examples)

Label Can Include:
- Badges: raw food, non gmo, bpa free, gluten free, halal etc
- anything you feel is appropriate

You can change the color of the logo(s) to Black, White, Silver or Gold.

Can you please include a mockup of your label design(s) on the supplied "Jar Mockup File". You can change the scene of the mockup if you like.

UPDATE:

Have decided on bee logo so please bo longer use the mountain logo for label mockups. Design(s) will need multiple color variations to represent the other MGO ratings, flavor combos and other honey types, other than manuka.

• Provide multiple designs for each honey type
Manuka Design
Spring Honey Design
MGO 100-1000 Design(s)
Wildflower Honey Design
Flavor Combo Honey Design

```html
<!DOCTYPE html>
<html lang="en">
<head>
<meta charset="utf-8">
<title>Hine Roa Honey – Manuka Honey Label</title>
<link href="https://fonts.googleapis.com/css2?family=Montserrat:wght@300;400;700&family=Nunito:wght@800&display=swap" rel="stylesheet">
<style>
  :root {
    --page: #ffffff;
    --label: #151515;
    --comb-light: #1f1f1f;
    --comb-dark: #111111;
    --gold: #d9b66f;
    --gold-deep: #a8843f;
    --cream: #e9e2d6;
  }
  html, body {
    margin: 0;
    padding: 0;
    width: 1200px;
    height: 725px;
    overflow: hidden;
    background: var(--page);
  }
  .canvas {
    position: relative;
    width: 1200px;
    height: 725px;
    background: var(--page);
  }
  .label {
    position: absolute;
    left: 40px;
    top: 40px;
    width: 1120px;
    height: 645px;
    background: var(--label);
    overflow: hidden;
  }
  .label__comb {
    position: absolute;
    inset: 18px 0 28px 0;
    background: radial-gradient(ellipse at center, var(--comb-light) 0%, var(--comb-dark) 100%);
  }
  .label__rule {
    position: absolute;
    left: 0;
    right: 0;
    height: 3px;
    background: var(--gold);
  }
  .label__rule--top { top: 10px; }
  .label__rule--bottom { bottom: 22px; }
  .label__rule--base { bottom: 10px; height: 2px; background: var(--gold-deep); }

  .brand-mark {
    position: absolute;
    left: 50%;
    top: 48px;
    width: 110px;
    height: 110px;
    margin-left: -55px;
    border: 2px solid var(--gold);
    border-radius: 50%;
    box-sizing: border-box;
  }
  .brand {
    position: absolute;
    left: 0;
    right: 0;
    top: 200px;
    text-align: center;
    font-family: "Montserrat", sans-serif;
    font-weight: 300;
    color: var(--gold);
    line-height: 1;
  }
  .brand__name {
    font-size: 44px;
    letter-spacing: 0.2em;
    padding-left: 0.2em;
  }
  .brand__suffix {
    display: block;
    font-size: 16px;
    letter-spacing: 0.1em;
    margin-top: 8px;
  }
  .product-name {
    position: absolute;
    left: 0;
    right: 0;
    top: 300px;
    margin: 0;
    text-align: center;
    font-family: "Nunito", sans-serif;
    font-weight: 800;
    font-size: 60px;
    letter-spacing: 0.02em;
    color: var(--gold);
    line-height: 1;
  }
  .origin {
    position: absolute;
    left: 0;
    right: 0;
    top: 388px;
    margin: 0;
    text-align: center;
    font-family: "Montserrat", sans-serif;
    font-weight: 400;
    font-size: 26px;
    color: var(--cream);
    line-height: 1;
  }
  .grade {
    position: absolute;
    left: 50%;
    top: 440px;
    width: 120px;
    height: 124px;
    margin-left: -60px;
  }
  .grade__shape {
    position: absolute;
    inset: 0;
    width: 120px;
    height: 124px;
  }
  .grade__value {
    position: absolute;
    left: 0;
    right: 0;
    top: 38px;
    text-align: center;
    font-family: "Montserrat", sans-serif;
    font-weight: 700;
    font-size: 20px;
    color: var(--label);
    line-height: 1;
  }
  .volume {
    position: absolute;
    right: 110px;
    top: 560px;
    font-family: "Montserrat", sans-serif;
    font-weight: 400;
    font-size: 30px;
    color: var(--cream);
    line-height: 1;
  }
</style>
</head>
<body>
<div class="canvas">
  <section class="label">
    <div class="label__comb" role="img" aria-label="Dark honeycomb hexagon pattern"></div>
    <div class="label__rule label__rule--top"></div>
    <div class="label__rule label__rule--bottom"></div>
    <div class="label__rule label__rule--base"></div>

    <div class="brand-mark" aria-hidden="true"></div>
    <div class="brand">
      <span class="brand__name">HINE ROA HONEY</span>
      <span class="brand__suffix">CO.</span>
    </div>
    <h1 class="product-name">MANUKA HONEY</h1>
    <p class="origin">PRODUCT OF NEW ZEALAND</p>

    <div class="grade">
      <svg class="grade__shape" viewBox="0 0 120 124" aria-hidden="true">
        <path d="M6 4 H114 V84 L60 120 L6 84 Z" fill="var(--gold)"/>
        <path d="M13 11 H107 V80 L60 111 L13 80 Z" fill="none" stroke="var(--label)" stroke-width="3"/>
      </svg>
      <span class="grade__value">MGO 820</span>
    </div>

    <span class="volume">250 ml</span>
  </section>
</div>
</body>
</html>
```